Website For Custom Home Builder

-Very elegant and simple design as I am a high end custom home builder.
-I build homes $2 million to $10 million range so the website needs to reflect the level of home that I build.
-Attached are photos of homes I have built to use as well as my logo.
-I need final design to be in layered format so my local guy can edit if he needs to.

3 Page Design
1. HomePage:
-logo, some photos,
-“Building beautiful custom homes in Indianapolis for over 20 years”
2. AboutPage:
-Wade Holloran has been building stunning custom homes in the Indianpolis area for over 20 years. As a small boutique building company we only build a handful of homes a year in order to offer our clients the personal attention that their homes deserve. It's this attention to detail that makes our client experience and final product something special and unique.
- family photo
3. ContactPage:
-office photo
-317-552-7190
-wade@whcrafted.com
-415 North Fernmill Rd, Suite 308, Carmel IN 46033

Target Market(s)

Very high end clients looking to build $2 million to $10 million homes.

Industry/Entity Type

Residential high end custom home builder/construction

Coding

Coded - Design and coding required

Number of Pages Required

3 page

Requirements
Must have
• Very simple and elegant design that represents the high end homes that I build.
Nice to have
Should not have
• Should NOT have a lot of clutter or be a very busy page from a design perspective.

```html
<!DOCTYPE html>
<html lang="en">
<head>
<meta charset="utf-8">
<title>Wade Holloran Custom Homes</title>
<link href="https://fonts.googleapis.com/css2?family=Poppins:wght@300;400;500;600&display=swap" rel="stylesheet">
<style>
:root{
  --brown-dark:#5c3117;
  --brown:#8a4a20;
  --brown-light:#a0592a;
  --cream:#faf6f1;
  --ink:#1e1510;
  --accent-text:#e08a4a;
  --white:#ffffff;
}
*{box-sizing:border-box;margin:0;padding:0}
html,body{width:679px;height:1200px;overflow:hidden;background:var(--white);font-family:"Poppins",sans-serif;color:var(--ink)}
.canvas{position:relative;width:679px;height:1200px}
.page{position:absolute;left:0;width:679px;background:var(--cream)}
.page-home{top:0;height:382px}
.page-about{top:396px;height:381px}
.page-contact{top:791px;height:409px}

.site-header{position:absolute;left:0;width:679px;background:var(--cream);border-top:1px solid var(--brown);border-bottom:1px solid var(--brown)}
.page-home .site-header{top:19px;height:35px;border-bottom-width:2px}
.page-about .site-header{top:19px;height:34px}
.page-contact .site-header{top:20px;height:34px}
.nav{position:absolute;left:90px;top:0;height:100%;display:flex;align-items:center;gap:0}
.nav a{position:absolute;font-size:7.5px;font-weight:500;color:var(--ink);text-decoration:none;white-space:nowrap;top:50%;transform:translateY(-50%)}
.nav a.active{color:var(--brown)}
.nav a.active::after{content:"";position:absolute;left:0;bottom:-4px;width:13px;height:1px;background:var(--brown)}
.nav .n-home{left:0}.nav .n-about{left:55px}.nav .n-contact{left:108px}
.brand{position:absolute;left:50%;top:50%;transform:translate(-50%,-50%);display:flex;align-items:center;gap:4px;font-size:10px;font-weight:500;letter-spacing:.5px;color:var(--ink);white-space:nowrap}
.brand-dot{width:7px;height:7px;background:var(--brown)}
.call-btn{position:absolute;left:526px;top:50%;transform:translateY(-50%);width:106px;height:21px;border-radius:11px;background:var(--brown);color:var(--white);font-size:7.5px;font-weight:600;display:flex;align-items:center;justify-content:center;gap:6px;letter-spacing:.3px}
.call-btn svg{width:10px;height:10px}

.site-footer{position:absolute;left:0;bottom:0;width:679px;height:21px;background:var(--brown-dark);color:var(--white);font-size:7px;font-weight:300;display:flex;align-items:center;justify-content:center}

.hero-photo{position:absolute;left:0;top:0;width:679px;height:361px;background:linear-gradient(100deg,#1f1d17 0%,#3a3124 35%,#6a5438 60%,#8a6a44 80%,#5a4430 100%)}
.hero-title{position:absolute;left:35px;top:217px;font-size:25px;line-height:32px;font-weight:500;color:var(--white);text-transform:uppercase;width:400px}
.slider-arrows{position:absolute;left:590px;top:263px;width:55px;height:27px;border-radius:14px;background:var(--white);display:flex;align-items:center;justify-content:center;gap:10px}
.slider-arrows svg{width:13px;height:10px}

.about-photo{position:absolute;left:34px;top:82px;width:263px;height:248px;background:linear-gradient(170deg,#b9d3e6 0%,#e6e0d4 40%,#9aa870 75%,#6f8c3c 100%)}
.eyebrow{position:absolute;left:325px;top:117px;font-size:8.5px;color:var(--brown);display:flex;align-items:center;gap:4px}
.eyebrow::after{content:"";width:30px;height:1px;background:var(--brown)}
.about-title{position:absolute;left:325px;top:138px;font-size:20.5px;line-height:26px;font-weight:500;text-transform:uppercase;width:260px}
.title-bar{position:absolute;left:325px;top:196px;width:58px;height:2px;background:var(--brown)}
.about-copy{position:absolute;left:325px;top:206px;width:255px;font-size:7.3px;line-height:12.3px;color:#4a3f38}

.contact-title{position:absolute;left:35px;top:117px;font-size:21.5px;font-weight:500;text-transform:uppercase}
.office-photo{position:absolute;left:246px;top:89px;width:399px;height:261px;background:linear-gradient(160deg,#e9ecec 0%,#c8cfcf 45%,#2d4a52 80%,#1c2a30 100%)}
.info-card{position:absolute;left:34px;top:156px;width:237px;height:173px;background:linear-gradient(180deg,var(--brown-dark) 0%,var(--brown-light) 100%)}
.info-row{position:absolute;left:15px;display:flex;align-items:center}
.info-icon{width:33px;height:33px;border:1px solid rgba(255,255,255,.45);border-radius:50%;display:flex;align-items:center;justify-content:center}
.info-icon svg{width:11px;height:11px}
.info-text{position:absolute;left:47px;white-space:nowrap}
.info-label{font-size:8.5px;color:var(--accent-text)}
.info-value{font-size:8px;font-weight:500;color:var(--white);line-height:12.5px;margin-top:3px}
.row-call{top:27px}.row-mail{top:70px}.row-loc{top:112px}
.row-call .info-text{top:0}.row-mail .info-text{top:0}.row-loc .info-text{top:-4px}
</style>
</head>
<body>
<div class="canvas">

  <section class="page page-home">
    <div class="hero-photo" role="img" aria-label="Luxury stone home at dusk with lit windows and a pool"></div>
    <header class="site-header">
      <nav class="nav"><a class="n-home active">Home</a><a class="n-about">About</a><a class="n-contact">Contact</a></nav>
      <div class="brand"><span class="brand-dot"></span>WADE HOLLORAN</div>
      <div class="call-btn"><svg viewBox="0 0 24 24" fill="none" stroke="#fff" stroke-width="2"><path d="M5 3h4l2 5-3 2a11 11 0 0 0 6 6l2-3 5 2v4a2 2 0 0 1-2 2A17 17 0 0 1 3 5a2 2 0 0 1 2-2z"/></svg>317-552-7190</div>
    </header>
    <h1 class="hero-title">Building beautiful custom homes in Indianapolis for over 20 years</h1>
    <div class="slider-arrows">
      <svg viewBox="0 0 26 20" fill="none" stroke="#1e1510" stroke-width="2"><path d="M25 10H2M10 2 2 10l8 8"/></svg>
      <svg viewBox="0 0 26 20" fill="none" stroke="#8a4a20" stroke-width="2"><path d="M1 10h23M16 2l8 8-8 8"/></svg>
    </div>
    <footer class="site-footer">© 2023 Wade Holloran. All Right Reserved.</footer>
  </section>

  <section class="page page-about">
    <header class="site-header">
      <nav class="nav"><a class="n-home">Home</a><a class="n-about active">About</a><a class="n-contact">Contact</a></nav>
      <div class="brand"><span class="brand-dot"></span>WADE HOLLORAN</div>
      <div class="call-btn"><svg viewBox="0 0 24 24" fill="none" stroke="#fff" stroke-width="2"><path d="M5 3h4l2 5-3 2a11 11 0 0 0 6 6l2-3 5 2v4a2 2 0 0 1-2 2A17 17 0 0 1 3 5a2 2 0 0 1 2-2z"/></svg>317-552-7190</div>
    </header>
    <div class="about-photo" role="img" aria-label="Family standing on the lawn in front of their new home"></div>
    <div class="eyebrow">ABOUT</div>
    <h2 class="about-title">Wade Holloran Custom Homes</h2>
    <div class="title-bar"></div>
    <p class="about-copy">Wade Holloran has been building stunning custom homes in the Indianpolis area for over 20 years. As a small boutique building company we only build a handful of homes a year in order to offer our clients the personal attention that their homes deserve. It's this attention to detail that makes our client experience and final product something special and unique.</p>
    <footer class="site-footer">© 2023 Wade Holloran. All Right Reserved.</footer>
  </section>

  <section class="page page-contact">
    <header class="site-header">
      <nav class="nav"><a class="n-home">Home</a><a class="n-about">About</a><a class="n-contact active">Contact</a></nav>
      <div class="brand"><span class="brand-dot"></span>WADE HOLLORAN</div>
      <div class="call-btn"><svg viewBox="0 0 24 24" fill="none" stroke="#fff" stroke-width="2"><path d="M5 3h4l2 5-3 2a11 11 0 0 0 6 6l2-3 5 2v4a2 2 0 0 1-2 2A17 17 0 0 1 3 5a2 2 0 0 1 2-2z"/></svg>317-552-7190</div>
    </header>
    <h2 class="contact-title">Contact Us</h2>
    <div class="office-photo" role="img" aria-label="Bright modern office interior with desks and shelving"></div>
    <div class="info-card">
      <div class="info-row row-call">
        <div class="info-icon"><svg viewBox="0 0 24 24" fill="none" stroke="#fff" stroke-width="2"><path d="M5 3h4l2 5-3 2a11 11 0 0 0 6 6l2-3 5 2v4a2 2 0 0 1-2 2A17 17 0 0 1 3 5a2 2 0 0 1 2-2z"/></svg></div>
        <div class="info-text"><div class="info-label">Call Us:-</div><div class="info-value">317-552-7190</div></div>
      </div>
      <div class="info-row row-mail">
        <div class="info-icon"><svg viewBox="0 0 24 24" fill="#fff"><path d="M2 5h20v14H2z"/><path d="M2 5l10 8 10-8" fill="none" stroke="#7a4019" stroke-width="2"/></svg></div>
        <div class="info-text"><div class="info-label">E-mail Us:-</div><div class="info-value">wade@whcrafted.com</div></div>
      </div>
      <div class="info-row row-loc">
        <div class="info-icon"><svg viewBox="0 0 24 24" fill="none" stroke="#fff" stroke-width="2"><path d="M12 21s-7-7-7-12a7 7 0 0 1 14 0c0 5-7 12-7 12z"/><circle cx="12" cy="9" r="2.5"/></svg></div>
        <div class="info-text"><div class="info-label">Location:-</div><div class="info-value">415 North Fernmill Rd, Suite 308,<br>Carmel IN 46033</div></div>
      </div>
    </div>
    <footer class="site-footer">© 2023 Wade Holloran. All Right Reserved.</footer>
  </section>

</div>
</body>
</html>
```